Website redesign for a Cloud Advisory business

We are looking to revisit our existing brand and website, with a view to updating both. Looking for concepts and designs for how the website might look, flow and feel. Current website is: www.brellomint.com.au

Scope and Deliverables: Concept design for the home page and one internal page.

We do not expect you to design all the pages and all the elements of the website at this stage.

This job is not for the full website design, but just for concepts that we can start with when we go into the full website design.

We would love to see a design feature based on our name, logo, or industry, which can run through banners and other collateral (twitter banner, ads on Google, corporate documents etc).

We want the brand to properly depict what we bring/deliver to businesses when consulting to them and this should extend to the colour scheme, logo, font (perhaps updated) and copy (which will be supplied).

Our brand should suitably communicate our ability, knowledge and extensive experience within the Cloud space.

It should express and evoke credibility, knowledge and understanding of the Cloud space, independence, gravitas, reliability, efficiency, trust, expertise, approachability, service delivery but be uncomplicated, practical and use plain speaking language.

Colours that reinforce this might include: Blues, blacks, silver, white, grey and our existing orange.

Website designs that we like or have referenced include:

Varnolift: http://varnolift.com.au/ - This has good information but looks a little amateur in it’s cartoon like design and colour scheme. Also, this seems to be aimed at clients more interested in price than design and what we are going for is a little more high end.

Pendramoor: https://www.pendramoor.com.au/ - This site has merit in its’ setup but little call to action on the home page, especially before the scroll line. I like the set up of the Case Studies page however I’d look to make it more prominent by having it set up 3 across rather than the 4 they have. Something such as this: https://www.qandelby.com/case-studies

Tolvane: http://www.tolvane.com.au/#home4 - This page is a good one as far as selling services and information on the company. I quite like it.

MirefoldIT: http://www.mirefoldit.com.au/ - While I don’t think is particularly creative, it does practically depict the services we offer in a fairly clear way and might be a bit of a basic (albeit dull) template to follow.

JDP: https://store.jdp.com/us/Product-Family/JDP-Advisory-Services/JDP-Cloud-Advisory-Service/p/JDP-Services-Cloud-Advisory - This offers substantial information but is probably a little confusing although the roll-over drop down menus have merit.

ZEV: http://www.zev.net.au/en/services/ - While this in not quite what we are looking for, the colour scheme gives it more gravitas and quality.

As another reference, this website and the way they present their case studies is also something we like, although I’d like them shown 3 up, side by side…. https://www.qandelby.com/case-studies.

We have added a page layout and page purpose document.

Target Market(s)

Corporates, small - medium business, direct referrals, via search results

Industry/Entity Type

Business

Number of Pages Required

1 page

Font styles to use
Sans Serif

Colors
85abd2
0455a3
000000
f37122
5c5c5c

Requirements
Must have
• Website must be mobile device compatible.
• Concept design for the home page.
Nice to have
• We would love to see a design feature based on our name, logo, or industry, which can run through banners and other collateral (twitter banner, ads on Google, corporate documents etc).

```html
<!DOCTYPE html>
<html lang="en">
<head>
<meta charset="utf-8">
<title>Brellomint – Cloud Advisory</title>
<link href="https://fonts.googleapis.com/css2?family=Lato:wght@300;400;700;900&display=swap" rel="stylesheet">
<style>
:root{
  --blue:#0455a3;
  --sky:#85abd2;
  --orange:#f37122;
  --ink:#000000;
  --grey:#5c5c5c;
  --light:#efefef;
  --line:#dddddd;
  --dark:#111418;
  --white:#ffffff;
}
*{box-sizing:border-box;margin:0;padding:0}
html,body{width:1200px;height:5341px;overflow:hidden}
body{font-family:'Lato',Arial,sans-serif;color:var(--grey);background:var(--white);position:relative;font-size:13px;line-height:1.6}
section,header,footer{position:absolute;left:0;width:1200px}
.wrap{position:relative;width:1060px;margin:0 auto;height:100%}
.title{font-size:34px;font-weight:700;color:#222;text-align:center}
.sub{text-align:center;font-size:13px;color:#666;width:520px;margin:6px auto 0}

/* header */
.topbar{top:0;height:46px;border-bottom:1px solid var(--line);font-size:12px;color:#777}
.topbar .wrap{display:flex;align-items:center;gap:28px}
.social{margin-left:auto;display:flex;gap:10px}
.social span{width:14px;height:14px;background:var(--blue);border-radius:50%}
.nav{top:46px;height:90px}
.nav .wrap{display:flex;align-items:center}
.brand{display:flex;align-items:center;gap:8px;font-size:26px;font-weight:900;color:#222}
.brand i{width:18px;height:18px;background:var(--orange);display:block}
.menu{margin-left:auto;display:flex;gap:34px;font-size:12px;font-weight:700;text-transform:uppercase;color:#444}
.menu a{color:inherit;text-decoration:none;padding:34px 0}
.menu a.on{color:var(--blue);border-top:3px solid var(--blue)}

/* hero */
.hero{top:136px;height:630px;background:linear-gradient(100deg,#05080d 0%,#0c1a2e 45%,#1f4f8a 70%,#0b1525 100%)}
.hero-copy{position:absolute;left:70px;top:200px;width:400px;color:var(--white)}
.hero-copy h1{font-size:40px;font-weight:900;line-height:1.1}
.hero-copy h2{font-size:30px;font-weight:400;margin-bottom:12px}
.hero-copy p{font-size:14px;color:#d6dde6}
.btn{display:inline-block;background:var(--orange);color:var(--white);font-size:12px;font-weight:700;padding:10px 18px;margin-top:22px;text-transform:uppercase}

/* industries */
.industries{top:766px;height:462px;padding-top:50px}
.industries .title{font-size:26px}
.ind-line{position:absolute;left:230px;right:230px;top:210px;border-top:1px solid var(--line)}
.ind-row{display:flex;justify-content:space-between;margin:45px 80px 0}
.ind{width:260px;text-align:center;position:relative}
.circle{width:100px;height:100px;border-radius:50%;background:var(--blue);margin:0 auto;display:flex;align-items:center;justify-content:center;border:6px solid #dbe6f2}
.ind h3{color:#222;font-size:16px;margin:24px 0 10px}
.ind p{font-size:12px;color:#888}

/* company */
.company{top:1228px;height:622px;background:var(--light);padding-top:48px}
.cards{display:flex;justify-content:center;gap:18px;margin-top:44px}
.card{width:222px;height:340px;position:relative;overflow:hidden}
.card .ph{height:340px;background:linear-gradient(160deg,#0e2544,#2a6fb8)}
.card .panel{position:absolute;left:0;right:0;bottom:0;height:165px;padding:16px;color:var(--white)}
.card h3{font-size:20px;font-weight:300;margin-bottom:6px}
.card p{font-size:12px;line-height:1.4}
.card .more{display:inline-block;margin-top:10px;background:rgba(0,0,0,.35);font-size:10px;font-weight:700;padding:5px 14px}
.p-blue{background:rgba(4,85,163,.92)}
.p-orange{background:rgba(228,146,24,.93)}
.p-grey{background:rgba(90,90,95,.9)}
.p-dark{background:rgba(15,15,18,.92)}

/* offer */
.offer{top:1850px;height:640px;padding-top:48px}
.orb{position:absolute;left:382px;top:162px;width:436px;height:436px;border-radius:50%;background:radial-gradient(circle,#2b2e33,#0a0b0d);color:var(--white);text-align:center;padding:120px 70px 0}
.orb h3{font-size:24px;font-weight:700;line-height:1.2;margin-bottom:12px}
.orb p{font-size:12px;color:#ccc}
.dot{position:absolute;width:62px;height:62px;border-radius:50%;background:var(--blue);border:4px solid var(--white);display:flex;align-items:center;justify-content:center;z-index:2}
.feat{position:absolute;width:170px;font-size:11px;line-height:1.5;color:#777}
.feat h4{color:#222;font-size:12px;margin-bottom:2px}
.feat.left{left:200px;text-align:right}
.feat.right{left:830px}

/* testimonial */
.testi{top:2490px;height:518px;background:linear-gradient(180deg,#0b0f16,#1b2431 60%,#0d1118);color:#dde;text-align:center}
.quote{color:var(--orange);font-size:60px;font-weight:900;line-height:1;padding-top:70px}
.testi p{width:940px;margin:10px auto 0;font-size:15px;line-height:1.7}
.avatar{width:80px;height:80px;border-radius:50%;background:#6f7885;margin:24px auto 8px}
.testi h4{color:var(--white);font-size:14px}
.dots{display:flex;justify-content:center;gap:8px;margin-top:16px}
.dots span{width:9px;height:9px;border-radius:50%;background:#777}
.dots span.on{background:var(--orange)}

/* faq */
.faq{top:3008px;height:692px}
.person{position:absolute;left:215px;top:110px;width:185px;height:560px;background:linear-gradient(180deg,#e8e4de,#8aa8c9);border-radius:60px 60px 8px 8px}
.qa{position:absolute;left:440px;top:135px;width:620px}
.qa h3{font-size:15px;color:#222;font-weight:400;margin-bottom:14px}
.item{border:1px solid #ccc;height:40px;margin-bottom:15px;display:flex;align-items:center;padding:0 16px;font-size:11px;color:#555;text-transform:uppercase}
.item b{margin-left:auto;color:#999;font-weight:400;font-size:16px}
.item.open{border-color:var(--blue);color:var(--blue)}
.answer{font-size:12px;color:#777;margin:-6px 0 20px}

/* blog */
.blog{top:3700px;height:625px;background:var(--light);padding-top:50px}
.posts{display:flex;justify-content:center;gap:24px;margin-top:40px}
.post{width:296px;background:var(--white)}
.post .ph{height:180px;background:linear-gradient(135deg,#0a2a5a,#3a86d0)}
.post .body{padding:14px 16px 20px}
.post h4{color:#222;font-size:15px}
.post small{font-size:11px;color:#999}
.post p{font-size:12px;margin-top:8px;color:#888}

/* contact */
.contact{top:4325px;height:675px;padding-top:50px}
.addr{position:absolute;left:140px;top:200px}
.addr .row{display:flex;gap:18px;margin-bottom:40px}
.ic{width:58px;height:58px;border-radius:50%;border:2px solid #ccc;display:flex;align-items:center;justify-content:center}
.addr h4{color:#222;font-size:15px;font-weight:400}
.addr p{font-size:11px;color:#888;line-height:1.5}
.form{position:absolute;left:430px;top:200px;width:560px;font-size:12px;color:#666}
.field{border-bottom:1px solid #ccc;height:44px;padding-top:6px}
.half{display:flex;gap:40px}
.half .field{flex:1}
.msg{height:130px;margin-top:20px}
.send{display:inline-block;background:var(--blue);color:var(--white);font-weight:700;padding:8px 26px;margin-top:22px}
.phones{position:absolute;left:1000px;top:200px;font-size:11px;color:#888;line-height:1.7}

/* footer */
.foot{top:5000px;height:305px;background:#111;color:#aaa;padding-top:40px}
.cols{display:flex;gap:60px;padding:0 10px}
.col{width:210px;font-size:11px;line-height:1.6}
.col h5{color:var(--white);font-size:14px;margin-bottom:14px}
.col li{list-style:none;margin-bottom:8px}
.col li::before{content:"›  ";color:var(--orange)}
.copy{position:absolute;left:0;width:1200px;top:5305px;height:36px;background:var(--blue);color:var(--white);text-align:center;font-size:12px;line-height:36px}
</style>
</head>
<body>

<header class="topbar"><div class="wrap">
  <span>(02) 5550 1847</span><span>info@brellomint.com.au</span>
  <div class="social"><span></span><span></span><span></span><span></span></div>
</div></header>

<header class="nav"><div class="wrap">
  <div class="brand"><i></i>Brellomint</div>
  <nav class="menu">
    <a class="on">Home</a><a>About Us</a><a>Industry Specialties</a><a>Solutions</a><a>Testimonials</a><a>FAQs</a><a>Contact Us</a>
  </nav>
</div></header>

<section class="hero" role="img" aria-label="Hand holding a glowing cloud network with connected device icons">
  <div class="hero-copy">
    <h1>IMPARTIAL CLOUD</h1>
    <h2>SOLUTIONS SYSTEM</h2>
    <p>Lorem Ipsum is simply dummy text of the printing and typesetting industry. Lorem Ipsum has been the industry's standard.</p>
    <span class="btn">Book a free consultation</span>
  </div>
</section>

<section class="industries">
  <h2 class="title">INDUSTRIES SPECIALITIES</h2>
  <p class="sub">Lorem Ipsum is simply dummy text of the printing and typesetting industry. Lorem Ipsum has been the industry's standard dummy text ever since the 1500s.</p>
  <div class="ind-line"></div>
  <div class="ind-row">
    <div class="ind"><div class="circle"><svg width="46" height="32" viewBox="0 0 46 32"><path d="M12 30a10 10 0 0 1 0-20 13 13 0 0 1 25 4 8 8 0 0 1-1 16z" fill="#fff"/></svg></div><h3>Lorem Ipsum Dolor Sit Amet</h3><p>Lorem Ipsum is simply dummy text of the printing and typesetting industry. Lorem Ipsum has been the standard text.</p></div>
    <div class="ind"><div class="circle"><svg width="46" height="40" viewBox="0 0 46 40"><path d="M12 24a10 10 0 0 1 0-20 13 13 0 0 1 25 4 8 8 0 0 1-1 16z" fill="#fff"/><path d="M23 24v10M13 34h20" stroke="#fff" stroke-width="2"/></svg></div><h3>Lorem Ipsum Dolor Sit Amet</h3><p>Lorem Ipsum is simply dummy text of the printing and typesetting industry. Lorem Ipsum has been the standard text.</p></div>
    <div class="ind"><div class="circle"><svg width="46" height="40" viewBox="0 0 46 40"><circle cx="23" cy="20" r="16" fill="none" stroke="#fff" stroke-width="3"/><path d="M7 20h32M23 4v32" stroke="#fff" stroke-width="2"/></svg></div><h3>Lorem Ipsum Dolor Sit Amet</h3><p>Lorem Ipsum is simply dummy text of the printing and typesetting industry. Lorem Ipsum has been the standard text.</p></div>
  </div>
</section>

<section class="company">
  <h2 class="title">The Company We Keep</h2>
  <p class="sub">Lorem Ipsum is simply dummy text of the printing and typesetting industry. Lorem Ipsum has been the industry's standard.</p>
  <div class="cards">
    <div class="card"><div class="ph" role="img" aria-label="Cloud services network graphic"></div><div class="panel p-blue"><h3>Cloud Services</h3><p>Lorem Ipsum is simply dummy text of the printing and typesetting industry.</p><span class="more">READ MORE</span></div></div>
    <div class="card"><div class="ph" role="img" aria-label="Server infrastructure graphic"></div><div class="panel p-orange"><h3>IT Infrastructure</h3><p>Lorem Ipsum is simply dummy text of the printing and typesetting industry.</p><span class="more">READ MORE</span></div></div>
    <div class="card"><div class="ph" role="img" aria-label="Digital circuit professional services graphic"></div><div class="panel p-grey"><h3>Professional Services</h3><p>Lorem Ipsum is simply dummy text of the printing and typesetting industry.</p><span class="more">READ MORE</span></div></div>
    <div class="card"><div class="ph" role="img" aria-label="Business meeting graphic"></div><div class="panel p-dark"><h3>Virtual CIO</h3><p>Lorem Ipsum is simply dummy text of the printing and typesetting industry.</p><span class="more">READ MORE</span></div></div>
  </div>
</section>

<section class="offer">
  <h2 class="title">What We Offer</h2>
  <p class="sub">Lorem Ipsum is simply dummy text of the printing and typesetting industry. Lorem Ipsum has been the industry's standard.</p>
  <div class="orb" role="img" aria-label="Dark textured circle behind quality statement">
    <h3>Quality &amp;<br>Professionalism</h3>
    <p>Lorem Ipsum is simply dummy text of the printing and typesetting industry. Lorem Ipsum has been the industry's standard dummy text ever since the 1500s, when an unknown printer took a galley of type and scrambled it to make a type specimen book.</p>
  </div>
  <div class="dot" style="left:413px;top:215px"><svg width="28" height="20"><path d="M8 18a6 6 0 0 1 0-12 8 8 0 0 1 15 2 5 5 0 0 1 0 10z" fill="#fff"/></svg></div>
  <div class="dot" style="left:725px;top:215px"><svg width="24" height="24"><circle cx="12" cy="12" r="9" fill="none" stroke="#fff" stroke-width="2"/><path d="M8 12l3 3 5-6" stroke="#fff" stroke-width="2" fill="none"/></svg></div>
  <div class="dot" style="left:413px;top:505px"><svg width="24" height="24"><circle cx="12" cy="8" r="4" fill="#fff"/><path d="M4 22a8 8 0 0 1 16 0z" fill="#fff"/></svg></div>
  <div class="dot" style="left:725px;top:505px"><svg width="24" height="24"><path d="M12 3l9 9-9 9-9-9z" fill="#fff"/></svg></div>
  <div class="feat left" style="top:180px"><h4>Cloud Advisory</h4>Lorem Ipsum is simply dummy text of the printing industry.</div>
  <div class="feat right" style="top:180px"><h4>Solution</h4>Lorem Ipsum is simply dummy text of the printing industry.</div>
  <div class="feat left" style="top:475px"><h4>Consulting</h4>Lorem Ipsum is simply dummy text of the printing industry.</div>
  <div class="feat right" style="top:475px"><h4>Integration</h4>Lorem Ipsum is simply dummy text of the printing industry.</div>
</section>

<section class="testi" role="img" aria-label="Dark background of a person typing on a laptop">
  <div class="quote">“</div>
  <p>Lorem Ipsum is simply dummy text of the printing and typesetting industry. Lorem Ipsum has been the industry's standard dummy text ever since the 1500s, when an unknown printer took a galley of type and scrambled it to make a type specimen book. It has survived not only five centuries, but also the leap into electronic typesetting, remaining essentially unchanged.</p>
  <div class="avatar" role="img" aria-label="Client portrait"></div>
  <h4>Mira Kestrel</h4>
  <small>Ceo blue star · Lorem Ipsum</small>
  <div class="dots"><span></span><span class="on"></span><span></span><span></span></div>
</section>

<section class="faq">
  <div class="person" role="img" aria-label="Standing man in white t-shirt and jeans"></div>
  <div class="qa">
    <h3>YOUR QUESTION , OUR ANSWER HERE</h3>
    <div class="item open">How does web hosting work?<b>−</b></div>
    <p class="answer">Lorem Ipsum is simply dummy text of the printing and typesetting industry. Lorem Ipsum has been the industry's standard dummy text ever since the 1500s, when an unknown printer took a galley of type and scrambled it to make a type specimen book. It has survived not only five centuries, but also the leap into electronic typesetting, remaining essentially unchanged.</p>
    <div class="item">How does web hosting work?<b>+</b></div>
    <div class="item">How does web hosting work?<b>+</b></div>
    <div class="item">How does web hosting work?<b>+</b></div>
    <div class="item">How does web hosting work?<b>+</b></div>
    <div class="item">How does web hosting work?<b>+</b></div>
  </div>
</section>

<section class="blog">
  <h2 class="title">Our Blog</h2>
  <p class="sub">Lorem Ipsum is simply dummy text of the printing and typesetting industry. Lorem Ipsum has been the industry's standard.</p>
  <div class="posts">
    <div class="post"><div class="ph" role="img" aria-label="Hand touching a blue digital screen"></div><div class="body"><h4>Image Post Format</h4><small>28 May, 2016 by Joe Doe</small><p>Lorem Ipsum is simply dummy text of the printing and typesetting industry, ever since the 1500s when an unknown printer took a galley.</p></div></div>
    <div class="post"><div class="ph" role="img" aria-label="Fingers on a glowing keyboard"></div><div class="body"><h4>Image Post Format</h4><small>28 May, 2016 by Joe Doe</small><p>Lorem Ipsum is simply dummy text of the printing and typesetting industry, ever since the 1500s when an unknown printer took a galley.</p></div></div>
    <div class="post"><div class="ph" role="img" aria-label="Hand holding a glowing globe network"></div><div class="body"><h4>Image Post Format</h4><small>28 May, 2016 by Joe Doe</small><p>Lorem Ipsum is simply dummy text of the printing and typesetting industry, ever since the 1500s when an unknown printer took a galley.</p></div></div>
  </div>
</section>

<section class="contact">
  <h2 class="title">Contact Us</h2>
  <p class="sub">Lorem Ipsum is simply dummy text of the printing and typesetting industry. Lorem Ipsum has been the industry's standard.</p>
  <div class="addr">
    <div class="row"><div class="ic"><svg width="20" height="24"><path d="M10 23s8-8 8-13a8 8 0 0 0-16 0c0 5 8 13 8 13z" fill="#555"/><circle cx="10" cy="10" r="3" fill="#fff"/></svg></div><div><h4>Address</h4><p>14 Harbour Lane, Sydney<br>NSW 2000, Australia</p></div></div>
    <div class="row"><div class="ic"><svg width="22" height="22"><path d="M5 2l4 4-2 3a12 12 0 0 0 6 6l3-2 4 4-3 3C9 20 2 13 2 5z" fill="#555"/></svg></div><div><h4>Free Helpline</h4><p>(02) 5550 1847<br>(02) 5550 2963</p></div></div>
    <div class="row"><div class="ic"><svg width="22" height="16"><rect x="1" y="1" width="20" height="14" fill="none" stroke="#555" stroke-width="2"/><path d="M1 1l10 8 10-8" stroke="#555" stroke-width="2" fill="none"/></svg></div><div><h4>Email</h4><p>info@brellomint.com.au<br>help@brellomint.com.au</p></div></div>
  </div>
  <div class="form">
    <div class="half"><div class="field">Full Name*</div><div class="field">Email*</div></div>
    <div class="field msg">Message</div>
    <span class="send">SEND</span>
  </div>
  <div class="phones">(02) 5550 7830<br>(02) 5550 4419</div>
</section>

<footer class="foot"><div class="wrap"><div class="cols">
  <div class="col"><h5>About Us</h5><p>Lorem Ipsum is simply dummy text of the printing and typesetting industry. Lorem Ipsum has been the industry's standard dummy text ever since the 1500s.</p><p style="margin-top:12px">An unknown printer took a galley of type and scrambled it to make a type specimen book.</p></div>
  <div class="col"><h5>Latest Posts</h5><ul><li>Lorem Ipsum is simply<br>October 15,2015</li><li>Lorem Ipsum is simply<br>October 15,2015</li><li>Lorem Ipsum is simply<br>October 15,2015</li><li>Lorem Ipsum is simply<br>October 15,2015</li></ul></div>
  <div class="col"><h5>Business Development</h5><ul><li>Technology</li><li>Cloud</li><li>Computing</li><li>Services</li><li>Access</li></ul></div>
  <div class="col"><h5>Contact Us</h5><p>(02) 5550 1847<br>info@brellomint.com.au</p><p style="margin-top:12px">The Innovators From<br>Mission Statement</p></div>
</div></div></footer>
<div class="copy">Copyright © 2015-2015 Brellomint, LLC. All rights reserved.</div>

</body>
</html>
```